Brightvault Banner Ad Campaign

Overview
We require 3 different banners within the same brief, but would like you to just produce 1 banner for your initial bid.

We require a punchy message to be delivered to existing poker players. We offer the opportunity for players to play poker with our money (ie. ‘staked’), sharing the profits if they win, us taking the losses if they lose. 'Sharks' is a poker term for skilled winning players who eat up the 'fish'.. term for unskilled losing players.

The players we stake are playing no risk poker and enjoy the support of our team, as well as professional coaching free of charge. Our key messages are bulleted below, some suggestions for tag lines also. We would like some creativity input in the design/ tag lines plus of course the banners themselves delivered. See www.brightvault-example.com for our colour scheme and shark fin logo and to get a feel for what we do.

3 different pieces of artwork required:-
2 'square', sized – 180x150
1 'normal' banner sized
Clearly we may want to resize these slightly for different uses.

Some messages we want to convey:-
• Free Bankroll $$$$
• Free Pro Coaching
• Part of a team & support network
• Risk free, stress free poker
• We are the best staking operation

Possible tag lines:-
Losing your bite?
Sharpen your teeth!
Get staked today!
Join the best, crush the rest

Thanks
Dorian
Updates

Guys,

we have a strong theme with the Shark and/or our red fin logo, can you focus on that in your designs please. a Shark as per brief is a successful poker player .. a 'fish' is what they prey on..

Thanks

Dorian

```html
<!DOCTYPE html>
<html lang="en">
<head>
<meta charset="utf-8">
<title>Brightvault Banner Ads</title>
<link href="https://fonts.googleapis.com/css2?family=Archivo+Black&family=Yellowtail&display=swap" rel="stylesheet">
<style>
  :root {
    --backdrop: #d9d9d9;
    --banner-dark: #1a0405;
    --banner-mid: #5a0c10;
    --banner-glow: #b3161d;
    --accent-red: #e0141c;
    --text-white: #ffffff;
    --text-light: #f2f2f2;
    --text-steel: #9a9a9a;
    --chip-dark: #220708;
    --chip-edge: #4a1315;
  }
  html, body {
    margin: 0;
    padding: 0;
    width: 1200px;
    height: 874px;
    overflow: hidden;
    background: var(--backdrop);
  }
  .stage {
    position: relative;
    width: 1200px;
    height: 874px;
  }
  .banner {
    position: absolute;
    top: 242px;
    width: 434px;
    height: 366px;
    overflow: hidden;
    font-family: "Archivo Black", "Arial Black", sans-serif;
    color: var(--text-white);
    box-shadow: 4px 6px 10px rgba(0,0,0,0.35);
    background:
      repeating-linear-gradient(135deg, rgba(255,255,255,0.03) 0 2px, transparent 2px 8px),
      radial-gradient(ellipse at 55% 25%, var(--banner-glow) 0%, var(--banner-mid) 45%, var(--banner-dark) 100%);
  }
  .banner--teeth { left: 113px; }
  .banner--best { left: 636px; }

  .chips-decor {
    position: absolute;
    left: -30px;
    top: 190px;
    width: 500px;
    height: 200px;
    background: radial-gradient(ellipse at 40% 45%, var(--chip-edge) 0%, var(--chip-dark) 55%, rgba(26,4,5,0) 80%);
  }
  .shark-photo {
    position: absolute;
    left: 156px;
    top: 118px;
    width: 290px;
    height: 240px;
    background: radial-gradient(ellipse at 50% 45%, #8c7a7c 0%, #5b3638 40%, rgba(60,10,12,0) 72%);
  }

  .headline {
    position: absolute;
    margin: 0;
    line-height: 1;
    white-space: nowrap;
    text-shadow: 2px 3px 4px rgba(0,0,0,0.6);
    transform-origin: top left;
  }
  .headline .red { color: var(--accent-red); }

  .sharpen { left: 19px; top: 62px; font-size: 76px; letter-spacing: -1px; }
  .your {
    position: absolute; left: 30px; top: 140px;
    font-family: "Yellowtail", cursive; font-size: 50px; line-height: 1;
    text-shadow: 2px 2px 3px rgba(0,0,0,0.6);
  }
  .teeth {
    left: 132px; top: 128px; font-size: 74px; letter-spacing: -1px;
    color: var(--text-light);
    text-shadow: 2px 3px 0 var(--text-steel), 4px 6px 6px rgba(0,0,0,0.6);
  }

  .join { left: 22px; top: 22px; font-size: 40px; letter-spacing: -1px; }
  .best {
    left: 214px; top: 14px; font-size: 64px; letter-spacing: -1px;
    transform: scaleY(1.45);
  }
  .crush { left: 108px; top: 98px; font-size: 34px; }
  .rest {
    left: 22px; top: 128px; font-size: 74px; letter-spacing: -1px;
    transform: scaleY(1.3);
  }

  .brand {
    position: absolute;
    top: 312px;
    display: flex;
    align-items: center;
    gap: 6px;
    font-family: "Archivo Black", "Arial Black", sans-serif;
    font-size: 20px;
    color: var(--text-white);
    letter-spacing: -0.5px;
  }
  .banner--teeth .brand { left: 136px; }
  .banner--best .brand { left: 14px; }
  .brand-dot {
    width: 14px; height: 14px; border-radius: 50%;
    background: var(--accent-red);
  }
</style>
</head>
<body>
<main class="stage">
  <section class="banner banner--teeth" aria-label="Sharpen your teeth banner">
    <div class="chips-decor" role="img" aria-label="Dark poker chips along the bottom edge"></div>
    <h2 class="headline sharpen">SH<span class="red">A</span>RPEN</h2>
    <span class="your">your</span>
    <p class="headline teeth">TEETH</p>
    <div class="brand"><span class="brand-dot"></span>Brightvault</div>
  </section>

  <section class="banner banner--best" aria-label="Join the best crush the rest banner">
    <div class="shark-photo" role="img" aria-label="Photo of a shark swimming in red-tinted water"></div>
    <p class="headline join">join the</p>
    <h2 class="headline best">BE<span class="red">$</span>T</h2>
    <p class="headline crush">crush the</p>
    <p class="headline rest">REST</p>
    <div class="brand"><span class="brand-dot"></span>Brightvault</div>
  </section>
</main>
</body>
</html>
```